Business card for a "family office" company

Please provide professional looking business card designs, incorporating the attached logo and below details. Harrowmere Holdings Pty Ltd is a family office / financial investment company. We are looking for a modern, professional and contemporary card design.

Industry/Entity Type

Finance

Contact Information for Business Card

Name: Dean Mollick
Title: Director
Company: Harrowmere Holdings Pty Ltd
Email: harrowdean@quillnet.example
Mobile: 0462 735 418
Address: 4/312 Barnaby Parade, Fernleigh Bay WA 6207, Australia

Requirements
Must have
• All details above and the logo. logo only on back side. incorporate colours of logo
Nice to have
• up to you
Should not have
• ?

```html
<!DOCTYPE html>
<html lang="en">
<head>
<meta charset="utf-8">
<title>Harrowmere Holdings – Business Card</title>
<link href="https://fonts.googleapis.com/css2?family=Open+Sans:wght@400;700&display=swap" rel="stylesheet">
<style>
  :root {
    --navy: #2c2a7c;
    --ink: #3a3a3f;
    --paper: #ffffff;
    --backdrop: #e6e6e8;
  }
  * { margin: 0; padding: 0; box-sizing: border-box; }
  html, body {
    width: 1200px;
    height: 840px;
    overflow: hidden;
    background: var(--backdrop);
    font-family: "Open Sans", Arial, sans-serif;
  }
  .sheet {
    width: 1200px;
    height: 840px;
    display: flex;
    align-items: center;
    justify-content: center;
    gap: 40px;
  }
  .card {
    position: relative;
    width: 540px;
    height: 328px;
    background: var(--paper);
    box-shadow: 0 2px 8px rgba(0,0,0,0.12);
    overflow: hidden;
  }

  /* Back side: company name */
  .card--back {
    display: flex;
    align-items: center;
    justify-content: center;
  }
  .brand {
    display: flex;
    align-items: center;
    gap: 14px;
  }
  .brand__mark {
    width: 34px;
    height: 34px;
    background: var(--navy);
    flex: none;
  }
  .brand__name {
    color: var(--navy);
    font-weight: 400;
    font-size: 24px;
    letter-spacing: 4px;
    text-transform: uppercase;
    white-space: nowrap;
  }

  /* Front side: contact details */
  .contact {
    position: absolute;
    left: 38px;
    top: 36px;
    color: var(--ink);
    font-size: 13px;
    line-height: 1.5;
  }
  .contact__name {
    color: var(--navy);
    font-weight: 700;
    font-size: 14px;
    text-transform: uppercase;
    line-height: 1.2;
  }
  .contact__title {
    color: var(--navy);
    font-size: 14px;
    text-transform: uppercase;
    line-height: 1.2;
    margin-bottom: 14px;
  }
  .contact__company { font-weight: 700; }
  .contact__gap { margin-top: 8px; }

  .accent-block {
    position: absolute;
    right: 0;
    bottom: 0;
    width: 230px;
    height: 150px;
    background: var(--navy);
  }
</style>
</head>
<body>
  <main class="sheet">
    <section class="card card--back" aria-label="Card back">
      <div class="brand">
        <span class="brand__mark"></span>
        <span class="brand__name">Harrowmere Holdings</span>
      </div>
    </section>

    <section class="card card--front" aria-label="Card front">
      <div class="contact">
        <p class="contact__name">Dean Mollick</p>
        <p class="contact__title">Director</p>
        <p class="contact__company">Harrowmere Holdings Pty Ltd</p>
        <p>4/312 Barnaby Parade</p>
        <p>Fernleigh Bay WA 6207, Australia</p>
        <p class="contact__gap">M : 0462 735 418</p>
        <p>harrowdean@quillnet.example</p>
        <p>harrowmereholdings.example</p>
      </div>
      <div class="accent-block"></div>
    </section>
  </main>
</body>
</html>
```